Executive search firm in fashion, luxury and retail industry needs logo and card design.

We are a start-up recruiting firm that specializes in the retail and fashion industry, based in New York. We are looking for something that will appeal to CEO level clients and candidates, but that has a little design edge...not overly corporate but still CEO-appropriate. We have clean, sophisticated taste and want a contemporary feel. Happy to have a two sided card. Not afraid of a little color but it should be high-design, not gimmicky and tasteful.

Quillby Market(s)

CEO's, HR Leaders, in retail, fashion (i.e. Havenmere, Quillby, Otto Vasquel)

Industry/Entity Type

Professional Service

Contact Information for Business Card

Linden Row Talent Partners
Address to be determined
New York, NY 10036

Marla Tovick
Managing Director
(555)013-2846
mtovick@lindenrowtalent.example

Font styles to use
Serif
Sans Serif

Requirements
Must have
• clean lines, crisp graphics, some color. Prefer a graphic treatment over a "logo" per se. No pictures, etc.
Nice to have
• double sided design.
Should not have
• Gimmicks, smaltz, goop. Think Gallery of Current Forms, not the Pelham Vault. No earth tones, as in beige and brown, no pastels. Strong colors are fine in moderation. Grays are good. Jewel tones are good. No red.

```html
<!DOCTYPE html>
<html lang="en">
<head>
<meta charset="utf-8">
<title>Linden Row Talent Partners – Business Card</title>
<link href="https://fonts.googleapis.com/css2?family=Open+Sans:wght@400;600&family=Raleway:wght@500&display=swap" rel="stylesheet">
<style>
  :root {
    --stage-top: #2a2a2a;
    --stage-bottom: #050505;
    --card-white: #ffffff;
    --brand-yellow: #efcf1f;
    --accent-yellow: #e8c21c;
    --mark-gray: #9c9a96;
    --ink: #2b2b2b;
    --ink-black: #111111;
  }
  * { margin: 0; padding: 0; box-sizing: border-box; }
  html, body { width: 1200px; height: 900px; overflow: hidden; }
  body {
    background: linear-gradient(180deg, var(--stage-top) 0%, #151515 55%, var(--stage-bottom) 100%);
    position: relative;
    font-family: "Open Sans", Arial, sans-serif;
  }
  .card {
    position: absolute;
    top: 306px;
    width: 440px;
    height: 271px;
    border-radius: 10px;
  }
  .card--front { left: 149px; background: var(--card-white); }
  .card--back { left: 608px; background: var(--brand-yellow); }

  .brand {
    position: absolute;
    display: flex;
    flex-direction: column;
    align-items: center;
    font-family: "Raleway", Arial, sans-serif;
    font-weight: 500;
    text-align: center;
    text-transform: uppercase;
  }
  .brand__dot { border-radius: 50%; }
  .brand__name { line-height: 1; letter-spacing: 0.02em; }
  .brand__sub { line-height: 1; margin-top: 5px; }

  .card--front .brand { left: 40px; top: 82px; width: 170px; color: var(--mark-gray); }
  .card--front .brand__dot { width: 34px; height: 34px; background: var(--mark-gray); margin-bottom: 14px; }
  .card--front .brand__name { font-size: 25px; }
  .card--front .brand__sub { font-size: 10px; }

  .card--back .brand { left: 0; width: 440px; top: 56px; color: var(--ink-black); }
  .card--back .brand__dot { width: 62px; height: 62px; background: var(--ink-black); margin-bottom: 24px; }
  .card--back .brand__name { font-size: 44px; }
  .card--back .brand__sub { font-size: 15px; margin-top: 7px; }

  .contact {
    position: absolute;
    left: 220px;
    top: 82px;
    color: var(--ink);
    font-size: 12px;
    line-height: 1.35;
  }
  .contact__name { color: var(--accent-yellow); font-weight: 600; font-size: 14.5px; }
  .contact__address { margin-top: 12px; }
  .contact__lines { margin-top: 14px; list-style: none; }
  .contact__lines li { display: flex; align-items: center; gap: 7px; height: 16px; }
  .contact__lines svg { width: 9px; height: 9px; flex: none; fill: var(--accent-yellow); }
</style>
</head>
<body>
  <section class="card card--front" aria-label="Card front">
    <div class="brand">
      <span class="brand__dot"></span>
      <span class="brand__name">Linden Row</span>
      <span class="brand__sub">Talent Partners</span>
    </div>
    <div class="contact">
      <p class="contact__name">Marla Tovick</p>
      <p class="contact__title">Managing Director</p>
      <p class="contact__address">New York, NY 10036</p>
      <ul class="contact__lines">
        <li>
          <svg viewBox="0 0 10 10" aria-hidden="true"><path d="M2 0.5 L3.6 0.5 L4.2 3 L3 3.8 C3.6 5.2 4.8 6.4 6.2 7 L7 5.8 L9.5 6.4 L9.5 8 C9.5 9 8.8 9.5 8 9.5 C4 9.3 0.7 6 0.5 2 C0.5 1.2 1 0.5 2 0.5 Z"/></svg>
          (555)013-2846
        </li>
        <li>
          <svg viewBox="0 0 10 10" aria-hidden="true"><path d="M0.5 2 H9.5 V8 H0.5 Z M1 2.3 L5 5.4 L9 2.3" stroke="#fff" stroke-width="0.7"/></svg>
          mtovick@lindenrowtalent.example
        </li>
      </ul>
    </div>
  </section>

  <section class="card card--back" aria-label="Card back">
    <div class="brand">
      <span class="brand__dot"></span>
      <span class="brand__name">Linden Row</span>
      <span class="brand__sub">Talent Partners</span>
    </div>
  </section>
</body>
</html>
```